Flyer for a cyber security training course which uses escape rooms

I want to design a flyer using the size DL (99 x 210 mm).
The flyer is to advertise the course titled: "Cyber Security Escape Room Training for Everybody". (Please note I changed the name, but if you did it under the old name I will evaluate based on the graphics and may get you to change the name for the final).
It is a half day, immersive, team based training session which uses interactive, hands on escape rooms to learn about cyber security.
Topics covered include: Phishing, Social Engineering, Physical Security, Social Media, Device Security, Passwords, Meta-Data, Encryption.
Either one of the Kelmore Vale Logos would be acceptable.
The QR code points to a promo video for the course: https://clipharbor.example/552093417
Enquires or bookings: growth@kelmorevale.edu.example

Target Market(s)

Companies wanting to ensure there staff know about cyber security

Industry/Entity Type

Corporate training, Local Government

Requirements
Must have
• Provided QR Code, contact details, Title of program

```html
<!DOCTYPE html>
<html lang="en">
<head>
<meta charset="utf-8">
<title>Cyber Security Escape Room Training for Everybody</title>
<link rel="stylesheet" href="https://fonts.googleapis.com/css2?family=League+Gothic&family=Arimo:wght@400;700&display=swap">
<style>
  :root {
    --ink: #000000;
    --paper: #ffffff;
    --signal: #ff0000;
    --panel-width: 588px;
  }
  * { margin: 0; padding: 0; box-sizing: border-box; }
  html, body {
    width: 1131px;
    height: 1200px;
    overflow: hidden;
    background: var(--paper);
  }
  .flyer {
    position: relative;
    width: 1131px;
    height: 1200px;
    background: var(--paper);
    overflow: hidden;
  }
  .flyer__dark-panel {
    position: absolute;
    left: 0; top: 0;
    width: var(--panel-width);
    height: 1200px;
    background: var(--ink);
  }
  .topic { position: absolute; }
  .topic__term {
    font-family: "League Gothic", "Oswald", sans-serif;
    font-weight: 400;
    font-size: 116px;
    line-height: 102px;
    letter-spacing: 0;
    text-transform: uppercase;
    white-space: nowrap;
    -webkit-text-stroke: 2.5px currentColor;
  }
  .topic__definition {
    font-family: "Arimo", "Helvetica Neue", Arial, sans-serif;
    font-size: 20.5px;
    line-height: 24px;
    margin-top: 6px;
  }
  .topic--left { left: 68px; width: 500px; }
  .topic--right { left: 612px; width: 500px; }

  .term--signal { color: var(--signal); }
  .term--light { color: var(--paper); }
  .term--dark { color: var(--ink); }
  .definition--light { color: var(--paper); }
  .definition--dark { color: var(--ink); }
  .definition--signal { color: var(--signal); }

  .course {
    position: absolute;
    left: 68px;
    top: 1078px;
    width: 500px;
    padding-top: 14px;
    border-top: 3px solid var(--signal);
  }
  .course__title {
    font-family: "League Gothic", "Oswald", sans-serif;
    font-weight: 400;
    font-size: 40px;
    line-height: 38px;
    text-transform: uppercase;
    color: var(--paper);
    -webkit-text-stroke: 1px currentColor;
  }
  .course__title-accent { color: var(--signal); }
  .course__summary {
    margin-top: 6px;
    font-family: "Arimo", "Helvetica Neue", Arial, sans-serif;
    font-size: 15px;
    line-height: 18px;
    color: var(--paper);
  }

  .contact {
    position: absolute;
    left: 612px;
    top: 1078px;
    width: 480px;
    padding-top: 14px;
    border-top: 3px solid var(--ink);
    display: flex;
    gap: 18px;
    align-items: flex-start;
  }
  .contact__qr {
    flex: 0 0 98px;
    width: 98px;
    height: 98px;
  }
  .contact__details {
    font-family: "Arimo", "Helvetica Neue", Arial, sans-serif;
    font-size: 15px;
    line-height: 19px;
    color: var(--ink);
  }
  .contact__org {
    font-weight: 700;
    font-size: 17px;
    margin-bottom: 4px;
  }
  .contact__label {
    color: var(--signal);
    font-weight: 700;
  }
</style>
</head>
<body>
<main class="flyer">
  <div class="flyer__dark-panel"></div>

  <section class="topic topic--left" style="top:44px">
    <h2 class="topic__term term--signal">Phishing</h2>
    <p class="topic__definition definition--light">fraudulent practice of sending emails or<br>other messages purporting to be from<br>reputable companies in order to induce<br>individuals to reveal personal information</p>
  </section>

  <section class="topic topic--left" style="top:270px">
    <h2 class="topic__term term--light">Meta-Data</h2>
    <p class="topic__definition definition--signal">a set of data that provides information<br>about other data, providing information<br>such as when and how it was gathered</p>
  </section>

  <section class="topic topic--left" style="top:470px">
    <h2 class="topic__term term--signal">Encryption</h2>
    <p class="topic__definition definition--light">the process of converting information or<br>data into a code, in order to prevent<br>unauthorized access</p>
  </section>

  <section class="topic topic--left" style="top:670px">
    <h2 class="topic__term term--light">Passwords</h2>
    <p class="topic__definition definition--signal">a secret word or phrase that must be<br>used to gain admission or access to<br>specific information or data</p>
  </section>

  <section class="topic topic--left" style="top:870px">
    <h2 class="topic__term term--signal">Social Media</h2>
    <p class="topic__definition definition--light">the means of interactions among people<br>in which they create, share &amp; exchange<br>information in virtual communities</p>
  </section>

  <section class="topic topic--right" style="top:46px">
    <h2 class="topic__term term--dark">Device<br>Security</h2>
    <p class="topic__definition definition--signal">the defense of IT assets against harm<br>and unauthorized use ranging from<br>securing desktop PCs, laptops,<br>smartphones, tablets, or Internet of<br>Things (IoT)</p>
  </section>

  <section class="topic topic--right" style="top:384px">
    <h2 class="topic__term term--signal">Social<br>Engineering</h2>
    <p class="topic__definition definition--dark">the use of deception to manipulate<br>people into revealing confidential<br>information or granting access to<br>systems, data or premises</p>
  </section>

  <section class="topic topic--right" style="top:720px">
    <h2 class="topic__term term--dark">Physical<br>Security</h2>
    <p class="topic__definition definition--signal">measures that are designed to deny<br>unauthorized access to facilities,<br>equipment, and resources and to<br>protect personnel and property<br>from damage or harm</p>
  </section>

  <section class="course">
    <h1 class="course__title">Cyber Security <span class="course__title-accent">Escape Room</span><br>Training for Everybody</h1>
    <p class="course__summary">Half-day, immersive, team-based training with hands-on escape rooms.</p>
  </section>

  <section class="contact">
    <svg class="contact__qr" viewBox="0 0 98 98" role="img" aria-label="QR code linking to the course promo video at https://clipharbor.example/552093417">
      <rect x="0" y="0" width="98" height="98" fill="#ffffff" stroke="#000000" stroke-width="3"/>
      <rect x="10" y="10" width="78" height="78" fill="#e6e6e6"/>
    </svg>
    <div class="contact__details">
      <p class="contact__org">Kelmore Vale</p>
      <p><span class="contact__label">Promo video</span><br>https://clipharbor.example/552093417</p>
      <p><span class="contact__label">Enquiries &amp; bookings</span><br>growth@kelmorevale.edu.example</p>
    </div>
  </section>
</main>
</body>
</html>
```